Modern & Simple Essential Oils Label

Company Name: Meadowlark Essentials

What we sell: Aromatherapy products, pure therapeutic essential oils.

Design need:
We are looking for a creative and youthful design for the labels used on small essentials oils.

I have two sizes of bottles that I use for essential oils a 5ml bottle and a 15ml bottle. They are dark Amber color glass with black lids. I like the clear labels or mayble a dark brown background. With white or clear lettering with punch of color too! Each oil type is represented by different color. (lavender- purple, lemon - yellow). The label will be the same for all the oils in the two sizes with only a different oil name & coordinating color.
5ml label size should be: 1 " x 2.625"
15ml label size should be: 1.5" x 3.5"

I have some labels that I have had another designer start on, but they aren't quite what I want and missing that something (alot!).. I don't know what. Interest maybe? Lack of design? I dunno.. they are attached. Maybe it's the logo? I don't know! But its gotta change! When I cut out a proof and put a sample on the bottle as I look straight on at the label all I see is a big dot, no logo.. nothing interesting.
Updates

Project Deadline Extended
Reason: Hi! Id like to extend this deadline. Ive been unavailable for a few days due to an illness and Im so far behind! Im feeling MUCH better and looking forward to getting caught up and move with the project. Im not sure how this works, but I attached a list of the oils that we currently have available. And in the list is the idea for the color schemes for the oils. The basic idea is for it to have a wide array of colors, so using different shades of greens, yellows, oranges and so on. So that its like a rainbow. We are not set of that particular color for that particular oil. It was just a idea list of possible colors for oils. Thanks so much!

Target Market(s)

Metro & Modern people. Interested in healthy organic living, Mostly women (some men) 20-45 who are interested in holistic healing.

Industry/Entity Type

It Company

Requirements
Must have
• A reputable look. Clean, organic, crisp, zen or spa-like feel. Modern, youthful appealing label design. Approachable and interesting, not intimidating so that I don't turn away people who are new or not familiar with how to use essential oils.
Should not have
• do NOT want the look to be anywhere close to medicinal, witchy, crafty, hippie, mystical, overly earthy, magical, or voodoo. Do not want it to look like something out of a grandmothers medicine cabinet.

```html
<!DOCTYPE html>
<html lang="en">
<head>
<meta charset="utf-8">
<title>Meadowlark Essentials – Essential Oil Labels</title>
<link rel="stylesheet" href="https://fonts.googleapis.com/css2?family=Roboto+Slab:wght@300;400;600&display=swap">
<style>
  :root {
    --canvas-light: #f4f4f4;
    --canvas-dark: #c9c9c9;
    --amber-deep: #2a1206;
    --amber-mid: #5a2510;
    --amber-glow: #7a3412;
    --ink-dark: #3a1a0c;
    --lemon: #e4e23c;
    --lavender: #c7abd9;
    --label-font: "Roboto Slab", Georgia, serif;
  }
  * { box-sizing: border-box; margin: 0; padding: 0; }
  html, body { width: 1200px; height: 900px; overflow: hidden; }
  body {
    background: radial-gradient(ellipse at 50% 40%, var(--canvas-light) 0%, #e2e2e2 55%, var(--canvas-dark) 100%);
    font-family: var(--label-font);
  }
  .label-sheet {
    position: absolute;
    inset: 0;
    display: flex;
    flex-direction: column;
    align-items: center;
    justify-content: center;
    gap: 60px;
  }
  .label-row { display: flex; gap: 40px; }

  .label {
    --accent: var(--lemon);
    position: relative;
    display: flex;
    flex-direction: column;
    align-items: center;
    justify-content: space-between;
    background: radial-gradient(ellipse at 50% 45%, var(--amber-glow) 0%, var(--amber-mid) 45%, var(--amber-deep) 100%);
    border-radius: 4px;
    overflow: hidden;
    color: var(--accent);
  }
  .label--lavender { --accent: var(--lavender); }
  .label--15ml { width: 525px; height: 225px; }
  .label--5ml { width: 394px; height: 150px; }

  .brand-band, .type-band {
    width: 100%;
    background: var(--accent);
    color: var(--ink-dark);
    text-align: center;
    line-height: 1;
    white-space: nowrap;
  }
  .brand-band { font-weight: 400; text-transform: lowercase; }
  .type-band { font-weight: 600; text-transform: uppercase; letter-spacing: 0.02em; }

  .oil-mark {
    flex: none;
    border-radius: 50%;
    background: var(--accent);
  }
  .oil-name {
    text-align: center;
    line-height: 1.05;
    color: var(--accent);
    white-space: nowrap;
  }
  .oil-name__lead { display: block; font-weight: 300; }
  .oil-name__main { display: block; font-weight: 600; }

  .label--15ml .brand-band { font-size: 17px; padding: 6px 0 5px; }
  .label--15ml .type-band { font-size: 16px; padding: 6px 0 5px; }
  .label--15ml .oil-mark { width: 40px; height: 40px; margin-top: 10px; }
  .label--15ml .oil-name { font-size: 25px; margin-bottom: 8px; }

  .label--5ml .brand-band { font-size: 12px; padding: 4px 0 3px; }
  .label--5ml .type-band { font-size: 11px; padding: 4px 0 3px; }
  .label--5ml .oil-mark { width: 26px; height: 26px; margin-top: 6px; }
  .label--5ml .oil-name { font-size: 16px; margin-bottom: 5px; }
</style>
</head>
<body>
  <main class="label-sheet">
    <div class="label-row">
      <section class="label label--15ml label--lemon">
        <div class="brand-band">Meadowlark Essentials</div>
        <div class="oil-mark"></div>
        <h2 class="oil-name"><span class="oil-name__lead">zesty</span><span class="oil-name__main">lemon</span></h2>
        <div class="type-band">Pure Essential Oil</div>
      </section>
      <section class="label label--15ml label--lavender">
        <div class="brand-band">Meadowlark Essentials</div>
        <div class="oil-mark"></div>
        <h2 class="oil-name"><span class="oil-name__lead">all about</span><span class="oil-name__main">lavender</span></h2>
        <div class="type-band">Pure Essential Oil</div>
      </section>
    </div>
    <div class="label-row">
      <section class="label label--5ml label--lemon">
        <div class="brand-band">Meadowlark Essentials</div>
        <div class="oil-mark"></div>
        <h2 class="oil-name"><span class="oil-name__lead">zesty</span><span class="oil-name__main">lemon</span></h2>
        <div class="type-band">Pure Essential Oil</div>
      </section>
      <section class="label label--5ml label--lavender">
        <div class="brand-band">Meadowlark Essentials</div>
        <div class="oil-mark"></div>
        <h2 class="oil-name"><span class="oil-name__lead">all about</span><span class="oil-name__main">lavender</span></h2>
        <div class="type-band">Pure Essential Oil</div>
      </section>
    </div>
  </main>
</body>
</html>
```